PowerPoint design of key models

We recently had a new PPT template created which we are very happy with. Now we want to have some of our key models on various pages in PPT to be reformatted and redesigned to match the other graphics of the new PT template. Can you please redesign the models and graphics so they have the same look and feel as the new template. I have included both files for you to work with. Thank you.

```html
<!DOCTYPE html>
<html lang="en">
<head>
<meta charset="utf-8">
<title>Key Models</title>
<link rel="stylesheet" href="https://fonts.googleapis.com/css2?family=Poppins:wght@400;500;600;700;800&display=swap">
<style>
:root{
  --navy:#172850;
  --blue:#0b7cc1;
  --mid:#2280c6;
  --sky:#3aabf0;
  --cyan:#21a9e1;
  --rule:#2a7fc4;
  --white:#ffffff;
  --ink:#111111;
}
html,body{margin:0;padding:0;overflow:hidden;background:var(--white);}
.canvas{width:1200px;height:758px;display:block;font-family:'Poppins',sans-serif;}
.title-xl{font-weight:700;font-size:27px;fill:var(--white);text-anchor:middle;}
.label-q{font-weight:500;font-size:23px;fill:var(--navy);}
.petal-title{font-weight:500;font-size:16px;fill:var(--navy);text-anchor:middle;}
.pill-item{font-weight:400;font-size:12px;fill:var(--white);}
.pill-left{text-anchor:end;}
.step-label{font-weight:500;font-size:21px;fill:var(--white);text-anchor:middle;}
.page-count{font-weight:600;font-size:18px;fill:var(--ink);text-anchor:end;}
.icon{fill:none;stroke:var(--white);stroke-width:3;stroke-linecap:round;stroke-linejoin:round;}
.icon-blue{fill:none;stroke:var(--cyan);stroke-width:3;stroke-linecap:round;stroke-linejoin:round;}
.divider{stroke:var(--rule);stroke-width:2;}
</style>
</head>
<body>
<svg class="canvas" viewBox="0 0 2408 1521" xmlns="http://www.w3.org/2000/svg">
  <defs>
    <linearGradient id="grad-blue" x1="0" y1="0" x2="0" y2="1">
      <stop offset="0" stop-color="#2280c6"/><stop offset="1" stop-color="#21a9e1"/>
    </linearGradient>
    <linearGradient id="grad-swoosh" x1="0" y1="0" x2="1" y2="0">
      <stop offset="0" stop-color="#21a9e1"/><stop offset="1" stop-color="#2270bd"/>
    </linearGradient>
    <linearGradient id="grad-arc" x1="0" y1="0" x2="0" y2="1">
      <stop offset="0" stop-color="#3aabf0" stop-opacity="0"/><stop offset=".2" stop-color="#3aabf0"/>
      <stop offset=".8" stop-color="#3aabf0"/><stop offset="1" stop-color="#3aabf0" stop-opacity="0"/>
    </linearGradient>
  </defs>

  <!-- grid dividers -->
  <line class="divider" x1="1276" y1="0" x2="1276" y2="1521"/>
  <line class="divider" x1="0" y1="709" x2="1266" y2="709"/>
  <line class="divider" x1="1282" y1="709" x2="2408" y2="709"/>
  <line class="divider" x1="0" y1="1441" x2="1266" y2="1441"/>
  <line class="divider" x1="1282" y1="1441" x2="2408" y2="1441"/>

  <!-- Model 1: task / team / individual -->
  <g class="model-three-circles">
    <g class="circle-task">
      <circle cx="636" cy="235" r="150" fill="none" stroke="var(--blue)" stroke-width="6"/>
      <circle cx="636" cy="235" r="136" fill="var(--blue)"/>
      <circle cx="636" cy="235" r="120" fill="none" stroke="var(--white)" stroke-width="4"/>
      <g class="icon">
        <path d="M602 190l6 6 12-12M602 212l6 6 12-12"/><rect x="600" y="226" width="14" height="14" rx="2"/>
        <rect x="626" y="186" width="44" height="12" rx="3"/><rect x="626" y="206" width="44" height="12" rx="3"/><rect x="626" y="226" width="44" height="12" rx="3"/>
      </g>
      <text class="title-xl" x="638" y="287">TASK</text>
    </g>
    <g class="circle-team">
      <circle cx="482" cy="482" r="150" fill="none" stroke="var(--blue)" stroke-width="6"/>
      <circle cx="482" cy="482" r="136" fill="var(--navy)"/>
      <circle cx="482" cy="482" r="120" fill="none" stroke="var(--white)" stroke-width="4"/>
      <g class="icon">
        <circle cx="480" cy="445" r="30"/><circle cx="480" cy="447" r="9"/><circle cx="458" cy="454" r="7"/><circle cx="502" cy="454" r="7"/>
        <path d="M462 490v-14a18 18 0 0 1 36 0v14M440 490v-10a14 14 0 0 1 20-12M520 490v-10a14 14 0 0 0-20-12M438 490h84"/>
      </g>
      <text class="title-xl" x="479" y="534">TEAM</text>
    </g>
    <g class="circle-individual">
      <circle cx="786" cy="482" r="150" fill="none" stroke="var(--blue)" stroke-width="6"/>
      <circle cx="786" cy="482" r="136" fill="var(--sky)"/>
      <circle cx="786" cy="482" r="120" fill="none" stroke="var(--white)" stroke-width="4"/>
      <g class="icon">
        <circle cx="794" cy="438" r="12"/><path d="M778 462a16 16 0 0 1 32 0"/>
        <path d="M750 470l20-10h30a6 6 0 0 1 0 12h-18M800 472l20-8a5 5 0 0 1 4 9l-30 14h-30M746 468l14 18-8 6-14-18z"/>
        <path d="M784 418l-4-6M794 414v-6M804 418l4-6"/>
      </g>
      <text class="title-xl" x="794" y="530">INDIVIDUAL</text>
    </g>
  </g>

  <!-- Model 2: questions / solutions / objections -->
  <g class="model-sales-cycle">
    <path d="M1610 84 A290 280 0 0 1 1610 640" fill="none" stroke="url(#grad-arc)" stroke-width="8"/>
    <path d="M1535 190 A182 182 0 1 0 1705 505 L1720 530 L1785 375 L1640 320 L1655 355 A115 115 0 1 1 1535 190 Z" fill="url(#grad-swoosh)"/>
    <path d="M1535 190 A182 182 0 0 1 1788 362 A130 120 0 0 0 1612 365 A130 130 0 0 1 1535 190 Z" fill="var(--navy)"/>
    <g class="step-question">
      <circle cx="1798" cy="142" r="62" fill="var(--white)"/>
      <circle cx="1798" cy="142" r="54" fill="var(--navy)"/>
      <g class="icon"><path d="M1798 118a24 24 0 1 1-12 44l-10 6 4-12a24 24 0 0 1 18-38z"/><path d="M1792 134a7 7 0 1 1 8 7v6"/><circle cx="1800" cy="154" r="1.5"/></g>
      <text class="label-q" x="1877" y="140">Question to Ask</text>
    </g>
    <g class="step-solutions">
      <circle cx="1897" cy="360" r="62" fill="var(--white)"/>
      <circle cx="1897" cy="360" r="54" fill="var(--mid)"/>
      <g class="icon"><circle cx="1902" cy="348" r="13"/><path d="M1897 362v8h10v-8M1878 380h20l14-8a5 5 0 0 1 4 8l-20 12h-18M1872 376v18"/><path d="M1902 326v-6M1888 330l-4-4M1916 330l4-4"/></g>
      <text class="label-q" x="1985" y="361">Solutions to needs?</text>
    </g>
    <g class="step-objections">
      <circle cx="1815" cy="567" r="62" fill="var(--white)"/>
      <circle cx="1815" cy="567" r="54" fill="var(--cyan)"/>
      <g class="icon"><path d="M1806 585v-30a4 4 0 0 1 8 0v-10a4 4 0 0 1 8 0v10a4 4 0 0 1 8 0v12l4-4a4 4 0 0 1 6 5l-10 16a14 14 0 0 1-12 6h-2a10 10 0 0 1-10-5zM1814 555v14M1822 555v14"/></g>
      <text class="label-q" x="1890" y="585">Objections to overcome?</text>
    </g>
  </g>

  <!-- Model 3: presence / questioning / behavioural flex / measurement -->
  <g class="model-four-petals">
    <circle cx="612" cy="1050" r="250" fill="none" stroke="var(--sky)" stroke-width="3"/>
    <circle cx="612" cy="1050" r="224" fill="none" stroke="var(--sky)" stroke-width="3"/>

    <rect x="162" y="820" width="300" height="170" rx="85" fill="var(--navy)"/>
    <rect x="760" y="813" width="306" height="169" rx="84" fill="var(--navy)"/>
    <rect x="162" y="1128" width="300" height="169" rx="84" fill="url(#grad-blue)"/>
    <rect x="760" y="1120" width="306" height="170" rx="85" fill="url(#grad-blue)"/>

    <path d="M338 912A125 125 0 0 1 588 912V1037H463A125 125 0 0 1 338 912Z" fill="url(#grad-blue)" stroke="var(--white)" stroke-width="10"/>
    <path d="M646 1027V912A116 116 0 0 1 878 912A116 116 0 0 1 762 1027Z" fill="var(--navy)" stroke="var(--white)" stroke-width="10"/>
    <path d="M463 1313A116 116 0 0 1 463 1083H578V1198A116 116 0 0 1 463 1313Z" fill="var(--navy)" stroke="var(--white)" stroke-width="10"/>
    <path d="M635 1073H762A125 125 0 1 1 635 1198Z" fill="url(#grad-blue)" stroke="var(--white)" stroke-width="10"/>

    <g class="petal-presence">
      <circle cx="463" cy="912" r="100" fill="var(--navy)"/><circle cx="463" cy="912" r="91" fill="var(--white)"/>
      <g class="icon-blue"><path d="M446 878a17 17 0 0 1 34 0c0 8-6 12-9 18h-16c-3-6-9-10-9-18zM455 900h16M457 908h12M463 868v28M455 876l8 6 8-6"/></g>
      <text class="petal-title" x="463" y="945">PRESENCE</text>
    </g>
    <g class="petal-questioning">
      <circle cx="762" cy="912" r="98" fill="var(--cyan)"/><circle cx="758" cy="910" r="92" fill="var(--white)"/>
      <g class="icon-blue"><path d="M764 860a28 28 0 1 1-16 52l-12 6 4-14a28 28 0 0 1 24-44z"/><path d="M756 878a8 8 0 1 1 10 8v8"/><circle cx="766" cy="902" r="1.5"/></g>
      <text class="petal-title" x="762" y="948">QUESTIONING</text>
    </g>
    <g class="petal-behavioural">
      <circle cx="463" cy="1198" r="98" fill="var(--cyan)"/><circle cx="466" cy="1196" r="92" fill="var(--white)"/>
      <g class="icon-blue"><path d="M440 1196v-12a26 26 0 1 1 40 0v6l6 8h-8v10"/><circle cx="462" cy="1162" r="7"/><circle cx="462" cy="1162" r="13"/></g>
      <text class="petal-title" x="463" y="1228">BEHAVIOURAL</text>
      <text class="petal-title" x="463" y="1249">FLEX</text>
    </g>
    <g class="petal-measurement">
      <circle cx="762" cy="1198" r="96" fill="var(--navy)"/><circle cx="760" cy="1196" r="91" fill="var(--white)"/>
      <g class="icon-blue"><rect x="744" y="1144" width="30" height="22" rx="3"/><path d="M751 1152h16M751 1159h10M736 1158v22h14l6 8 6-8h24v-20"/></g>
      <text class="petal-title" x="762" y="1216">MEASUREMENT</text>
      <text class="petal-title" x="762" y="1237">&amp; FEEDBACK</text>
    </g>

    <g class="pill-item pill-left">
      <text x="316" y="875">Logged On ‹</text><text x="316" y="896">Mindful state ‹</text>
      <text x="316" y="917">Manage climate ‹</text><text x="316" y="938">Observations ‹</text>
      <text x="316" y="1188">From High Control ‹</text><text x="316" y="1209">To Low Control ‹</text>
    </g>
    <g class="pill-item">
      <text x="924" y="875">› Ask, don't Tel</text><text x="924" y="896">› Use a Variety of</text>
      <text x="924" y="917">› Questions</text>
      <text x="924" y="1190">› 5 levels of Listening</text><text x="924" y="1211">› Be an Active Listener</text>
    </g>
  </g>

  <!-- Model 4: plan / recruit / execute / sustain -->
  <g class="model-arrow-steps">
    <polygon points="2172,895 2335,1075 2172,1255" fill="var(--cyan)"/>
    <rect x="1398" y="1004" width="760" height="144" fill="var(--navy)"/>
    <polygon points="2148,885 2315,1075 2148,1265" fill="var(--navy)"/>

    <g stroke="var(--white)" stroke-width="2" fill="var(--sky)">
      <line x1="1513" y1="1050" x2="1513" y2="1100"/><circle cx="1513" cy="1101" r="4"/>
      <line x1="1681" y1="1070" x2="1681" y2="1115"/><circle cx="1681" cy="1069" r="4"/>
      <line x1="1864" y1="1050" x2="1864" y2="1100"/><circle cx="1864" cy="1101" r="4"/>
      <line x1="2032" y1="1070" x2="2032" y2="1115"/><circle cx="2032" cy="1069" r="4"/>
    </g>

    <g class="step-circles">
      <circle cx="1515" cy="997" r="58" fill="var(--white)"/><circle cx="1515" cy="997" r="51" fill="url(#grad-blue)"/>
      <circle cx="1683" cy="1170" r="58" fill="var(--white)"/><circle cx="1683" cy="1170" r="51" fill="url(#grad-blue)"/>
      <circle cx="1864" cy="997" r="58" fill="var(--white)"/><circle cx="1864" cy="997" r="51" fill="url(#grad-blue)"/>
      <circle cx="2035" cy="1170" r="58" fill="var(--white)"/><circle cx="2035" cy="1170" r="51" fill="url(#grad-blue)"/>
    </g>
    <g class="icon">
      <path d="M1496 980h36a10 10 0 0 1 0 20h-24a10 10 0 0 0 0 20h36"/><circle cx="1494" cy="980" r="4"/><path d="M1540 1020v-16h8v8h-8"/>
      <path d="M1666 1148l20 24M1676 1144l8 8-8 6-8-8zM1694 1150h12M1698 1158h8M1662 1190a8 8 0 0 1 16 0M1688 1190a8 8 0 0 1 16 0"/><circle cx="1670" cy="1176" r="5"/><circle cx="1696" cy="1176" r="5"/>
      <rect x="1838" y="980" width="22" height="28" rx="2"/><path d="M1843 988h12M1843 996h12"/><rect x="1870" y="994" width="20" height="26" rx="2"/><circle cx="1866" cy="974" r="8"/><circle cx="1860" cy="1014" r="6"/>
      <circle cx="2028" cy="1162" r="14"/><circle cx="2028" cy="1162" r="5"/><circle cx="2048" cy="1184" r="10"/><circle cx="2048" cy="1184" r="3"/>
    </g>
    <text class="step-label" x="1515" y="1129">PLAN</text>
    <text class="step-label" x="1685" y="1049">RECRUIT</text>
    <text class="step-label" x="1866" y="1129">EXECUTE</text>
    <text class="step-label" x="2033" y="1049">SUSTAIN</text>
  </g>

  <text class="page-count" x="2384" y="1500">X14</text>
</svg>
</body>
</html>
```